Business Card Design for Tarlo Cosmetics

hair extension supplier and mobile technican
make up and make up artistry
cosmetic eye contacts
eye lashes
general facial and hair products

```html
<!DOCTYPE html>
<html lang="en">
<head>
<meta charset="utf-8">
<title>Tarlo Cosmetics – Business Card</title>
<link rel="stylesheet" href="https://fonts.googleapis.com/css2?family=Josefin+Sans:wght@400&family=Kalam:wght@400&family=Arimo:wght@400&display=swap">
<style>
  :root {
    --page-bg: #ffffff;
    --card-light: #ffffff;
    --card-dark: #000000;
    --ink-dark: #1c1c1c;
    --ink-light: #ffffff;
    --muted: #9a9a9a;
    --frame: #8e8e8e;
    --skin: #d9a98f;
    --skin-shadow: #6b4a3a;
  }
  * { margin: 0; padding: 0; box-sizing: border-box; }
  html, body {
    width: 1200px; height: 800px; overflow: hidden;
    background: var(--page-bg);
  }
  .sheet { position: relative; width: 1200px; height: 800px; }

  .size-note {
    position: absolute; right: 796px; text-align: right;
    font-family: "Arimo", Arial, sans-serif;
    font-size: 30px; color: var(--muted); line-height: 1;
  }
  .size-note--cm { top: 345px; }
  .size-note--mm { top: 400px; }

  .card {
    position: absolute; left: 476px; width: 560px; height: 312px;
    overflow: hidden;
  }
  .card--front {
    top: 71px; background: var(--card-light);
    border: 2px solid var(--frame);
  }
  .card--back { top: 421px; background: var(--card-dark); }

  .wordmark {
    font-family: "Josefin Sans", Arial, sans-serif;
    font-weight: 400; text-transform: uppercase; line-height: 1;
  }
  .wordmark__main { display: block; }
  .wordmark__sub { display: block; }

  .card--front .wordmark {
    position: absolute; left: 0; right: 0; top: 98px;
    text-align: center; color: var(--ink-dark);
  }
  .card--front .wordmark__main { font-size: 54px; letter-spacing: 16px; margin-right: -16px; }
  .card--front .wordmark__sub { font-size: 16px; letter-spacing: 9px; margin-right: -9px; margin-top: 12px; }

  .holder-name {
    font-family: "Kalam", "Comic Sans MS", cursive;
    font-weight: 400; line-height: 1;
  }
  .card--front .holder-name {
    position: absolute; left: 0; right: 0; top: 218px;
    text-align: center; font-size: 27px; color: var(--muted); letter-spacing: 2px;
  }

  .portrait {
    position: absolute; left: 0; top: 0; width: 200px; height: 100%;
    background:
      radial-gradient(ellipse 70px 110px at 55px 110px, var(--skin) 0%, rgba(217,169,143,0.6) 55%, rgba(0,0,0,0) 100%),
      radial-gradient(ellipse 60px 70px at 50px 250px, #b08a3e 0%, rgba(90,70,30,0.5) 50%, rgba(0,0,0,0) 100%),
      linear-gradient(90deg, var(--skin-shadow) 0%, #2a1d17 55%, var(--card-dark) 100%);
  }

  .card--back .wordmark {
    position: absolute; right: 40px; top: 60px;
    text-align: center; color: var(--ink-light);
  }
  .card--back .wordmark__main { font-size: 30px; letter-spacing: 10px; margin-right: -10px; }
  .card--back .wordmark__sub { font-size: 10px; letter-spacing: 5px; margin-right: -5px; margin-top: 7px; }

  .contact {
    position: absolute; right: 36px; top: 168px;
    text-align: right; color: var(--ink-light);
    font-family: "Arimo", Arial, sans-serif; font-size: 15px; line-height: 1.2;
  }
  .card--back .holder-name { font-size: 26px; letter-spacing: 1px; margin-bottom: 4px; }
  .contact__address { margin-bottom: 11px; }
</style>
</head>
<body>
<main class="sheet">
  <p class="size-note size-note--cm">9 c.m. x 5 c.m.</p>
  <p class="size-note size-note--mm">90 m.m. x 50 m.m.</p>

  <section class="card card--front" aria-label="Business card front">
    <h1 class="wordmark">
      <span class="wordmark__main">Tarlo</span>
      <span class="wordmark__sub">Cosmetics</span>
    </h1>
    <p class="holder-name">Mirela Santori</p>
  </section>

  <section class="card card--back" aria-label="Business card back">
    <div class="portrait" role="img" aria-label="Beauty portrait photograph of a model with red lips and a gold chain necklace against a dark background with golden bokeh lights"></div>
    <h2 class="wordmark">
      <span class="wordmark__main">Tarlo</span>
      <span class="wordmark__sub">Cosmetics</span>
    </h2>
    <address class="contact" style="font-style: normal;">
      <p class="holder-name">Mirela Santori</p>
      <p class="contact__address">27 Halden st, Eastvale, WA, 6010</p>
      <p class="contact__phone">mobile 0400 12 34 56</p>
      <p class="contact__email">mirela@tarlocosmetics.com.au</p>
    </address>
  </section>
</main>
</body>
</html>
```